Covid-19 Mortgage Housing Market Coaching

I need a one page 8.5 x 11 printable infographic to describe the following:
Housing and Mortgage Market Coach
Through your Employer Home-ownership Benefit
The Coronavirus has resulted in an unprecedented Government coordination to reduce the spread of the virus, as such, has altered the way we live and work.
As each of us looks to the potential impact of the Coronavirus to our financial stability, it can be difficult to obtain trusted information to help make sound financial decisions.
As part of your employee home ownership program through your employer, you have access to this educational coaching on the below topics:
• What is happening in the stock market and why it is happening.
• Motivation behind Feds cutting rates and how that translates to the lending market.
• Discuss the future of interest rates.
• Discuss the future of the housing market. How will the spring and summer housing markets be effected?
• Everyone says to refinance now. Is that really in my best interest? Learn how to do a refinance analysis and determine if refinancing is right for you.
Having a better understanding of what is happening in the financial markets, with interest rates and the housing market can help you successfully navigate this rapidly evolving situation.
Please be sure that our phone number is prominently displayed 1-800-555-0182 and our web address www.lanternroofguild.com

```html
<!DOCTYPE html>
<html lang="en">
<head>
<meta charset="utf-8">
<title>Market Coach – Housing | Mortgage</title>
<link rel="stylesheet" href="https://fonts.googleapis.com/css2?family=Oswald:wght@500;600&family=Open+Sans:wght@400;600&display=swap">
<style>
  :root {
    --navy: #1f3a6b;
    --green: #2e8b3e;
    --leaf: #5db947;
    --ink: #4a4a4a;
    --paper: #ffffff;
    --backdrop: #3b3b3d;
  }
  * { margin: 0; padding: 0; box-sizing: border-box; }
  html, body {
    width: 1200px; height: 2475px; overflow: hidden;
    background: var(--backdrop);
  }
  body { position: relative; }
  .flyer {
    position: absolute; left: 0; top: 461px;
    width: 1200px; height: 1553px; overflow: hidden;
    background: var(--paper);
    font-family: "Open Sans", Arial, sans-serif;
  }
  .masthead__title, .masthead__subtitle, .masthead__tagline {
    position: absolute; left: 0; right: 0; text-align: center;
    font-family: "Oswald", "Arial Narrow", sans-serif; font-weight: 600;
    line-height: 1; white-space: nowrap;
  }
  .masthead__title {
    top: 100px; font-size: 68px; color: var(--navy);
    letter-spacing: 19px; text-indent: 19px;
  }
  .masthead__subtitle {
    top: 183px; font-size: 46px; color: var(--green);
    letter-spacing: 11px; text-indent: 11px;
  }
  .masthead__rule {
    position: absolute; left: 298px; top: 233px; width: 596px; height: 2px;
    background: var(--green);
  }
  .masthead__tagline {
    top: 247px; font-size: 20px; color: var(--green);
    letter-spacing: 3.5px; text-indent: 3.5px;
  }
  .copy { position: absolute; left: 77px; width: 1030px; letter-spacing: 2.4px; font-weight: 600; font-size: 18.5px; line-height: 24px; }
  .copy--intro { top: 380px; color: var(--navy); }
  .copy--intro p + p { margin-top: 2px; }
  .copy--lead { top: 541px; color: var(--green); }
  .copy--close { top: 810px; color: var(--green); text-align: justify; }
  .topics {
    position: absolute; left: 92px; top: 632px; width: 1010px; list-style: none;
    color: var(--ink); font-size: 16px; line-height: 24px; letter-spacing: 1.8px;
  }
  .topics li { position: relative; padding-left: 16px; }
  .topics li:last-child { line-height: 20px; margin-top: 5px; }
  .topics li::before {
    content: ""; position: absolute; left: 2px; top: 9px;
    width: 6px; height: 6px; border-radius: 50%; background: var(--green);
  }
  .topics li:last-child::before { top: 7px; }
  .hero-art {
    position: absolute; left: 60px; top: 900px; width: 1068px; height: 490px;
    background: linear-gradient(90deg, #eef6ea 0%, #6cbf4e 14%, #3f9e37 58%, #d6d6d6 66%, #f0f0f0 100%);
  }
  .brand { position: absolute; left: 70px; top: 1416px; display: flex; align-items: center; gap: 14px; }
  .brand__mark { width: 28px; height: 28px; background: var(--leaf); }
  .brand__name { font-weight: 600; font-size: 30px; line-height: 40px; color: var(--navy); letter-spacing: -0.5px; }
  .contact {
    position: absolute; left: 722px; top: 1427px; font-style: normal;
    color: var(--green); font-weight: 600; font-size: 25px; line-height: 33px; letter-spacing: 3.6px;
  }
</style>
</head>
<body>
  <main class="flyer">
    <header class="masthead">
      <h1 class="masthead__title">MARKET COACH</h1>
      <h2 class="masthead__subtitle">HOUSING | MORTGAGE</h2>
      <div class="masthead__rule"></div>
      <p class="masthead__tagline">THROUGH YOUR EMPLOYER HOME-OWNERSHIP BENEFIT</p>
    </header>

    <section class="copy copy--intro">
      <p>The Coronavirus has resulted in an unprecedented Government coordination to reduce the spread of the virus, as such, has altered the way we live and work.</p>
      <p>As each of us looks to the potential impact of the Coronavirus to our financial stability, it can be difficult to obtain trusted information to help make sound financial decisions.</p>
    </section>

    <p class="copy copy--lead">As part of your employee home ownership program through your employer, you have access to this educational coaching on the below topics:</p>

    <ul class="topics">
      <li>What is happening in the stock market and why it is happening.</li>
      <li>Motivation behind Feds cutting rates and how that translates to the lending market.</li>
      <li>Discuss the future of interest rates.</li>
      <li>Discuss the future of the housing market. How will the spring and summer housing markets be effected?</li>
      <li>Everyone says to refinance now. Is that really in my best interest? Learn how to do a refinance analysis<br>and determine if refinancing is right for you.</li>
    </ul>

    <p class="copy copy--close">Having a better understanding of what is happening in the financial markets, with interest rates and the housing market can help you successfully navigate this rapidly evolving situation.</p>

    <div class="hero-art" role="img" aria-label="Row of green paper houses leading to a large white house, each with a virus particle at its base"></div>

    <div class="brand">
      <span class="brand__mark"></span>
      <span class="brand__name">Lantern Roof Guild</span>
    </div>

    <address class="contact">
      <div class="contact__phone">1-800-555-0182</div>
      <div class="contact__web">www.lanternroofguild.com</div>
    </address>
  </main>
</body>
</html>
```